Need flyer for honey

I need the advertising flyer for my honey products. Will need around 4-6 page A5 size. Flyer content is ready but will need to check the wording and need the artwork and pictures designed in a proper manner.

```html
<!DOCTYPE html>
<html lang="en">
<head>
<meta charset="utf-8">
<title>Why Australian Honey? – Flyer</title>
<link rel="stylesheet" href="https://fonts.googleapis.com/css2?family=Courgette&family=Lato:ital,wght@1,400&display=swap">
<style>
  :root {
    --bg: #e9e4dc;
    --orange: #f7a21a;
    --orange-deep: #f08a10;
    --red: #e8461c;
    --cream: #fdf3c8;
    --cream-light: #fffbe6;
    --text: #3b2c1c;
    --white: #ffffff;
  }
  html, body {
    margin: 0;
    padding: 0;
    width: 825px;
    height: 1200px;
    overflow: hidden;
    background: var(--bg);
  }
  .canvas {
    position: relative;
    width: 825px;
    height: 1200px;
  }
  .flyer {
    position: absolute;
    left: 12px;
    top: 33px;
    width: 668px;
    height: 945px;
    transform: scale(1.2);
    transform-origin: 0 0;
    overflow: hidden;
    background: linear-gradient(180deg, var(--cream) 0%, var(--cream-light) 55%, var(--cream) 100%);
    box-shadow: 0 3px 10px rgba(0,0,0,0.25);
  }
  .flyer-shapes {
    position: absolute;
    inset: 0;
  }
  .title-small, .title-large, .section-heading, .contact-line {
    font-family: "Courgette", cursive;
    position: absolute;
    margin: 0;
    font-weight: 400;
    white-space: nowrap;
  }
  .title-small {
    left: 316px;
    top: 24px;
    font-size: 31px;
    color: var(--white);
  }
  .title-large {
    left: 385px;
    top: 58px;
    font-size: 60px;
    line-height: 1;
    color: var(--red);
  }
  .section-heading {
    left: 34px;
    font-size: 19px;
    color: var(--red);
  }
  .section-copy {
    position: absolute;
    left: 34px;
    width: 598px;
    margin: 0;
    font-family: "Lato", sans-serif;
    font-style: italic;
    font-size: 12.2px;
    line-height: 16px;
    color: var(--text);
    text-align: justify;
  }
  .section-copy.narrow { width: 414px; }
  .contact-line {
    left: 36px;
    font-size: 19px;
    color: var(--red);
  }
</style>
</head>
<body>
<div class="canvas">
  <article class="flyer">
    <svg class="flyer-shapes" width="668" height="945" viewBox="0 0 668 945">
      <defs>
        <linearGradient id="bandGrad" x1="0" y1="0" x2="0" y2="1">
          <stop offset="0" stop-color="#f9b126"/>
          <stop offset="1" stop-color="#f59a12"/>
        </linearGradient>
        <radialGradient id="honeyGrad" cx="0.5" cy="0.5" r="0.6">
          <stop offset="0" stop-color="#f6d27a"/>
          <stop offset="1" stop-color="#c97b12"/>
        </radialGradient>
      </defs>
      <path d="M0 0 H668 V118 C600 150 540 192 470 192 C380 192 300 150 200 130 C120 115 40 130 0 140 Z" fill="url(#bandGrad)"/>
      <path d="M200 126 C300 146 380 186 470 186 C540 186 600 148 668 112 V124 C600 160 540 198 470 198 C380 198 300 158 200 136 Z" fill="var(--white)"/>
      <path d="M200 134 C300 156 380 196 470 196 C540 196 600 160 668 124 V140 C600 176 540 206 470 206 C380 206 300 166 200 140 Z" fill="var(--red)"/>
      <rect role="img" aria-label="Honeycomb pieces with a wooden honey dipper and a pool of honey" x="28" y="8" width="180" height="160" rx="40" fill="url(#honeyGrad)"/>
      <rect role="img" aria-label="Small glass jar of honey with a dipper resting on top" x="205" y="82" width="130" height="80" rx="14" fill="url(#honeyGrad)"/>
      <path d="M668 610 C640 690 590 740 520 790 L668 790 Z" fill="var(--red)"/>
      <path d="M668 640 C645 710 600 760 540 800 L668 800 Z" fill="var(--orange)"/>
      <path d="M0 822 C150 805 300 830 430 840 C520 846 600 820 668 790 V945 H0 Z" fill="url(#bandGrad)"/>
      <path d="M0 818 C150 800 300 826 430 836 C520 842 600 816 668 786 V792 C600 822 520 850 430 844 C300 834 150 810 0 826 Z" fill="var(--red)"/>
      <path d="M0 826 C150 810 300 834 430 844 C520 850 600 824 668 792 V798 C600 830 520 856 430 850 C300 840 150 818 0 832 Z" fill="var(--white)"/>
      <circle cx="588" cy="752" r="76" fill="var(--red)"/>
      <circle cx="588" cy="752" r="68" fill="var(--white)"/>
      <circle role="img" aria-label="Close-up of a honey dipper in a glass bowl of honey" cx="588" cy="752" r="64" fill="url(#honeyGrad)"/>
      <circle cx="433" cy="860" r="72" fill="var(--red)"/>
      <circle cx="433" cy="860" r="64" fill="var(--white)"/>
      <circle role="img" aria-label="Honey dripping from a dipper into a jar" cx="433" cy="860" r="60" fill="url(#honeyGrad)"/>
    </svg>

    <h1 class="title-small">Why Australian</h1>
    <p class="title-large">Honey?</p>

    <h2 class="section-heading" style="top:186px">Clean &amp; Chemical Free</h2>
    <p class="section-copy" style="top:228px">Unlike many other countries producing honey, Australia has miles of pristine native forests and diverse native flowers that are chemical free which provides the clean honey nectar resources. Meanwhile, the honey bee industry is well protected by the Australia Quarantine and Inspection Service which keeps industry free from varroa mite and other exotic diseases. Very rare the chemicals are used in diseases control. Therefore from the very original source, Australia honey is clean than from any other part of the world.</p>

    <h2 class="section-heading" style="top:323px">Pure &amp; Healthy</h2>
    <p class="section-copy" style="top:374px">Honey is healthy food, while many overseas honey producers are commercialized, who would minimize the honey production circle to enhance production and adulterate their honey to make it a common consistency. Color and flavor are controlled by adding additives, sugars, syrups and extenders.</p>
    <p class="section-copy" style="top:436px">On the other hand, the Australian honey bee industry has a commitment to purity. Australian honey producers do not use any of the additives or sugars to make their honey better looking. Instead, they insist to make honey that is 100% pure and natural. Honey is left in the hives to let bee fan it until the water content drops to a certain level while the nutrition level is protected and raised.</p>

    <h2 class="section-heading" style="top:518px">Unique Taste</h2>
    <p class="section-copy" style="top:553px">Australia is home to more than ten thousand species of plants and flowers, many of which are found nowhere else in the world. The country's unique native Eucalyptus trees and flowers create distinctive flavors of honey. From dark amber to golden light in the color, Australia honey delivers various tastes from gentle sweetness and mild caramel like to noticeable fragrance and sweet. Out of which everyone can find a taste of his own.</p>

    <h2 class="section-heading" style="top:638px; left:37px">Safety assured</h2>
    <p class="section-copy narrow" style="top:684px">As a country prioritizes its people's health and safety, the Australia government and regulation bodies have established the world's most strict food safety standards. There are also strict quality control procedures in the honey &amp; bee industry that all apiarists and honey packers must adhere to. Therefore, Australia is the rare country in the world that has very low risk of contamination from honey collection to packing and to distribution.</p>

    <p class="contact-line" style="top:868px">Contact us:555.010.2040</p>
    <p class="contact-line" style="top:897px">Visit us: www.goldhive.example</p>
  </article>
</div>
</body>
</html>
```